Vocational Mentor needs an impressive business card

1. I need a business card (or maybe three with identic look) to promote me and my three business titles/services:
- Vocational Mentor. I help people find their vocation and live happily from it. I use my 20 years of experience in business, management and psychology to help them identify the most efficient ways to make a living doing what they are passionate about.
- Business Angel. I help founders start a succesful business with minimum risks and costs. I use my 20 years of experience in sales, management and entrepreneurship to help them identify the most efficient ways, in terms of time and cost, to validate their business idea.
- Learning Designer. I design unique learning programs that produce long-term cognitive and behavioural changes to people and organisations. I use my 20 years of experience in learning, teaching and change management to create minimalist experiences and processes that allow them to change efficiently in their pursued direction.

2. I would like a two-sided business card, on the front with my name, contact details and titles, on the back the explanation of the services.
Updates

Hi all,

I updated my brief, included contacts info and give feedback on all designs I got. I am new on this platform so please tell me if you need anything else or if I don't use corectly the platform forms.

Kind regards,
Tudor

Hi all,

I shortened the services description by deleting the phrase "I call..."

Kind regards,
Tudor

Target Market(s)

Freelancers, startups, people and organization willing to invest in change through ultimate learning experiences

Industry/Entity Type

Business

Font styles to use
Serif

Requirements
Must have
• Front side: full name, titles, web site, email, phone like below:
Tudor Vasilache
Vocational Mentor, Business Angel, Learning Designer
info@tudorvasilache.example
www.tudorvasilache.example
+40-745-TUDORV
Nice to have
• Back side: the description of the services I provide as in the task description.
1/3: it would be nice if I can jam all three titles on the front side but then I need a solution to jam all three services on the back side.

```html
<!DOCTYPE html>
<html lang="en">
<head>
<meta charset="utf-8">
<title>Business Card – Services</title>
<link href="https://fonts.googleapis.com/css2?family=Hind:wght@300;400&family=Hind+Siliguri:wght@600&family=Gudea:ital@1&display=swap" rel="stylesheet">
<style>
  :root {
    --accent: #f2a731;
    --paper: #ffffff;
    --ink: #111111;
    --on-accent: #ffffff;
  }
  html, body {
    margin: 0;
    padding: 0;
    overflow: hidden;
    background: var(--paper);
  }
  .card {
    position: relative;
    width: 1200px;
    height: 777px;
    background: var(--paper);
    overflow: hidden;
  }
  .identity-band {
    position: absolute;
    left: 0;
    top: 0;
    width: 230px;
    height: 100%;
    background: var(--accent);
  }
  .identity {
    position: absolute;
    left: 58px;
    bottom: 14px;
    transform-origin: left bottom;
    transform: rotate(-90deg) translateY(100%);
    white-space: nowrap;
    color: var(--on-accent);
  }
  .identity-name {
    display: block;
    font-family: "Hind Siliguri", sans-serif;
    font-weight: 600;
    font-size: 56px;
    line-height: 62px;
  }
  .identity-email {
    display: block;
    font-family: "Hind", sans-serif;
    font-weight: 300;
    font-size: 38px;
    line-height: 46px;
  }
  .services {
    position: absolute;
    left: 300px;
    top: 0;
    right: 0;
    list-style: none;
    margin: 0;
    padding: 0;
  }
  .service {
    position: absolute;
    left: 0;
    width: 860px;
  }
  .service:nth-child(1) { top: 82px; }
  .service:nth-child(2) { top: 325px; }
  .service:nth-child(3) { top: 568px; }
  .service-check {
    position: absolute;
    left: 0;
    top: 26px;
    width: 44px;
    height: 44px;
  }
  .service-title {
    margin: 0 0 0 100px;
    font-family: "Hind", sans-serif;
    font-weight: 300;
    font-size: 80px;
    line-height: 92px;
    color: var(--ink);
    letter-spacing: 1px;
  }
  .service-text {
    margin: 0 0 0 100px;
    font-family: "Gudea", sans-serif;
    font-style: italic;
    font-size: 31px;
    line-height: 44px;
    color: var(--ink);
    width: 740px;
  }
</style>
</head>
<body>
<main class="card">
  <aside class="identity-band">
    <div class="identity">
      <span class="identity-name">Name Surname</span>
      <span class="identity-email">name@domain.com</span>
    </div>
  </aside>
  <ul class="services">
    <li class="service">
      <svg class="service-check" viewBox="0 0 44 44" aria-hidden="true"><rect x="2" y="2" width="40" height="40" fill="none" stroke="#111" stroke-width="4"/></svg>
      <h2 class="service-title">Vocational trainer</h2>
      <p class="service-text">your text on this service can be written here to explain the service or sell it</p>
    </li>
    <li class="service">
      <svg class="service-check" viewBox="0 0 44 44" aria-hidden="true"><rect x="2" y="2" width="40" height="40" fill="none" stroke="#111" stroke-width="4"/></svg>
      <h2 class="service-title">Business Angel</h2>
      <p class="service-text">your text on this service can be written here to explain the service or sell it</p>
    </li>
    <li class="service">
      <svg class="service-check" viewBox="0 0 44 44" aria-hidden="true"><rect x="2" y="2" width="40" height="40" fill="none" stroke="#111" stroke-width="4"/></svg>
      <h2 class="service-title">Learning Designer</h2>
      <p class="service-text">your text on this service can be written here to explain the service or sell it</p>
    </li>
  </ul>
</main>
</body>
</html>
```